Tot Petal Product Label for Tear-Free Head-to-Toe Wash

Need a bottle label design for a new line of natural products targeting infants and children. Products are Pediatrician-developed and paraben-free, sulfate-free, fragrance-free, and cruelty-free. Design should be clean and have a high-end feel to it. Will need other product labels in Tot Petal line designed as well in upcoming projects.

Target Market(s)

Newborn to young elementary age children and their parents

Industry/Entity Type

Cosmetics/Beauty

Font styles to use
Other font styles liked:
• Brand fonts are Jost and Sonorous

Colors

Designer to choose colors to be used in the design.

Requirements
Must have
• Tot Petal logo, Pediatrician Developed logo, and a clean high-end feel to it. The label must fit the specialty bottle we will be using (label measurements and diagram will be provided) for the front and back of bottle only (NOT the side labels). It must include our list of ingredients (will provide once designer selected).
Nice to have
• Should stand out on the shelf of other baby products due to it's clean simplicity and high-end feel
Should not have
• too much of a "kiddie" feel to it (targeting the parents not the kids)

```html
<!DOCTYPE html>
<html lang="en">
<head>
<meta charset="utf-8">
<title>Tot Petal — Wash Label Dielines</title>
<link rel="stylesheet" href="https://fonts.googleapis.com/css2?family=Jost:wght@500;600&display=swap">
<style>
  :root {
    --paper: #ffffff;
    --dieline: #3bb4ea;
    --frame-outer: #e6cfc6;
    --frame-inner: #c99a72;
    --ink: #7a5a14;
    --blush: #f2b8c6;
    --blush-deep: #e9a2b4;
    --sand: #ecd7c4;
  }
  html, body {
    margin: 0;
    padding: 0;
    width: 1200px;
    height: 1200px;
    overflow: hidden;
    background: var(--paper);
  }
  .label-sheet {
    display: block;
    width: 1200px;
    height: 1200px;
  }
  .dieline {
    fill: none;
    stroke: var(--dieline);
    stroke-width: 3;
  }
  .frame-outer {
    fill: none;
    stroke: var(--frame-outer);
    stroke-width: 5;
  }
  .frame-inner {
    fill: none;
    stroke: var(--frame-inner);
    stroke-width: 5;
  }
  .text-guide { fill: none; stroke: none; }
  .brand-name {
    font-family: "Jost", sans-serif;
    font-weight: 600;
    fill: var(--ink);
    text-anchor: middle;
  }
  .tagline {
    font-family: "Jost", sans-serif;
    font-weight: 600;
    fill: var(--ink);
    text-anchor: middle;
  }
</style>
</head>
<body>
<svg class="label-sheet" viewBox="0 0 1660 1660" xmlns="http://www.w3.org/2000/svg">
  <defs>
    <radialGradient id="artwork-blush" cx="50%" cy="60%" r="60%">
      <stop offset="0%" stop-color="var(--blush)"/>
      <stop offset="100%" stop-color="var(--blush-deep)"/>
    </radialGradient>
    <linearGradient id="artwork-sand" x1="0" y1="0" x2="0" y2="1">
      <stop offset="0%" stop-color="#ffffff"/>
      <stop offset="100%" stop-color="var(--sand)"/>
    </linearGradient>
    <clipPath id="clip-front-inner">
      <rect x="237" y="351" width="541" height="969" rx="270"/>
    </clipPath>
    <clipPath id="clip-back-inner">
      <rect x="1072" y="492" width="430" height="768" rx="215"/>
    </clipPath>
    <path id="front-name-arc" class="text-guide" d="M177,790 A335,335 0 0 1 847,790"/>
    <path id="front-tagline-arc" class="text-guide" d="M292,810 A220,220 0 0 0 732,810"/>
    <path id="back-name-arc" class="text-guide" d="M1008,840 A280,280 0 0 1 1568,840"/>
    <path id="back-tagline-arc" class="text-guide" d="M1127,870 A165,165 0 0 0 1457,870"/>
  </defs>

  <!-- Front label -->
  <g class="label label--front">
    <path class="dieline" d="M127,1377 V460 C127,400 160,365 205,346 Q505,230 810,346 C852,364 882,400 882,460 V1377 Z"/>
    <rect class="frame-outer" x="205" y="316" width="606" height="1040" rx="303"/>
    <rect class="frame-inner" x="237" y="351" width="541" height="969" rx="270"/>
    <text class="brand-name" font-size="60" letter-spacing="14">
      <textPath href="#front-name-arc" startOffset="50%">TOT PETAL</textPath>
    </text>
    <circle cx="518" cy="775" r="145" fill="url(#artwork-blush)" role="img" aria-label="Illustration of a sleeping baby under a soft sunrise"/>
    <text class="tagline" font-size="27" letter-spacing="4">
      <textPath href="#front-tagline-arc" startOffset="50%">NATURALLY, FOR EVERY BABY</textPath>
    </text>
    <rect x="237" y="1095" width="541" height="230" fill="url(#artwork-sand)" clip-path="url(#clip-front-inner)" role="img" aria-label="Gentle water wave pattern"/>
  </g>

  <!-- Back label -->
  <g class="label label--back">
    <path class="dieline" d="M1033,1377 V440 C1033,405 1050,383 1075,370 Q1288,270 1495,370 C1522,383 1540,405 1540,440 V1377 Z"/>
    <rect class="frame-outer" x="1047" y="463" width="480" height="825" rx="240"/>
    <rect class="frame-inner" x="1072" y="492" width="430" height="768" rx="215"/>
    <text class="brand-name" font-size="48" letter-spacing="11">
      <textPath href="#back-name-arc" startOffset="50%">TOT PETAL</textPath>
    </text>
    <circle cx="1296" cy="828" r="112" fill="url(#artwork-blush)" role="img" aria-label="Illustration of a sleeping baby under a soft sunrise"/>
    <text class="tagline" font-size="21" letter-spacing="3">
      <textPath href="#back-tagline-arc" startOffset="50%">NATURALLY, FOR EVERY BABY</textPath>
    </text>
    <rect x="1072" y="1080" width="430" height="185" fill="url(#artwork-sand)" clip-path="url(#clip-back-inner)" role="img" aria-label="Gentle water wave pattern"/>
  </g>
</svg>
</body>
</html>
```